Qualifying Builders Questionnaire

We need a questionnaire designed to send out to potential clients with qualifying questions

Industry/Entity Type

Building

Colors

Designer to choose colors to be used in the design.

```html
<!DOCTYPE html>
<html lang="en">
<head>
<meta charset="utf-8">
<title>Qualifying Builders Questionnaire</title>
<link href="https://fonts.googleapis.com/css2?family=Roboto+Condensed:wght@400;700&family=Mulish:wght@300;400&display=swap" rel="stylesheet">
<style>
:root{
  --page:#f7f3f3;
  --white:#ffffff;
  --red:#e0232a;
  --pink-top:#fbe4e7;
  --pink-bottom:#eab9c0;
  --ink:#1b1b1b;
  --muted:#8d8d8d;
  --field:#ffffff;
  --note-bg:#f1f1f1;
  --dark:#3a3a3a;
}
*{box-sizing:border-box;margin:0;padding:0}
html,body{width:1146px;height:1200px;overflow:hidden}
body{background:var(--page);font-family:"Mulish",sans-serif;color:var(--muted);position:relative}
.browser-note{position:absolute;left:153px;top:12px;width:130px;text-align:center;font:700 7.5px/1.3 "Roboto Condensed",sans-serif;color:#555}
.browser-note a{color:var(--red);text-decoration:underline}
.column{position:absolute;background:var(--white);box-shadow:0 0 8px rgba(0,0,0,.06)}
.col-one{left:50px;top:52px;width:338px;height:1160px;border-radius:6px 6px 0 0}
.col-two{left:402px;top:50px;width:338px;height:1160px}
.col-three{left:763px;top:50px;width:337px;height:289px;background:var(--white);border-radius:0 0 6px 6px;overflow:hidden}
.brand{height:72px;display:flex;flex-direction:column;align-items:center;justify-content:center;gap:3px;border-bottom:3px solid var(--red)}
.brand-mark{width:14px;height:14px;background:var(--red)}
.brand-name{font:700 12px/1 "Roboto Condensed",sans-serif;color:var(--red);letter-spacing:.5px;text-transform:uppercase}
.details{position:relative;height:222px;background:linear-gradient(var(--pink-top),var(--pink-bottom));padding:16px 0 0 28px;display:flex;gap:36px}
.details::after{content:"";position:absolute;left:158px;bottom:-8px;border:8px solid transparent;border-bottom:none;border-top-color:var(--pink-bottom)}
.field-group{width:123px}
.group-title{font:700 10px/1 "Roboto Condensed",sans-serif;color:var(--red);margin-bottom:8px;white-space:nowrap}
.field{height:19px;border-radius:10px;background:var(--field);font-size:7.5px;line-height:19px;padding-left:11px;margin-bottom:8px;color:#9a9a9a}
.radio-line{font:italic 400 7.5px/1 "Roboto Condensed",sans-serif;color:var(--ink);margin:-2px 0 7px;display:flex;align-items:center;gap:4px}
.radio-line::before{content:"";width:5px;height:5px;border-radius:50%;background:var(--red)}
.form{padding:20px 0 0 28px}
.col-two .form{padding:14px 0 0 29px}
.q{font:700 9.6px/1.2 "Roboto Condensed",sans-serif;color:var(--ink)}
.sub{font-size:8.4px;color:var(--ink);margin-top:4px}
.hint{font-size:7.6px;color:var(--muted);margin-top:4px}
.opt{font-size:7.6px;height:20.3px;line-height:20.3px;color:var(--muted);white-space:nowrap}
.opt.wrap{white-space:normal;line-height:1.3;height:auto;padding:3px 0 6px}
.opts{margin-top:1px}
.block{margin-top:16px}
.small-q{font:700 7.8px/1.3 "Roboto Condensed",sans-serif;color:var(--ink);margin-top:6px}
.link{font:400 7.8px/1.3 "Roboto Condensed",sans-serif;color:var(--red);text-decoration:underline}
.para{font-size:7.6px;line-height:1.6;color:var(--muted);margin:10px 16px 0 0}
.note{background:var(--note-bg);font:400 7px/1.75 "Roboto Condensed",sans-serif;color:var(--ink);padding:9px 8px}
.col-two .note{margin:10px 14px 0 0}
.col-three .note{margin:0 14px 0 21px;padding-top:1px}
.tick-title{font:700 7.8px/1 "Roboto Condensed",sans-serif;color:var(--ink);margin:21px 0 0 27px}
.col-three .opt{padding-left:27px}
.agree{font-size:7.6px;line-height:1.3;color:var(--muted);margin:14px 14px 6px 27px}
.submit{display:inline-block;margin:6px 0 0 27px;width:85px;height:22px;background:var(--red);color:#fff;font:700 7.8px/22px "Roboto Condensed",sans-serif;text-align:center}
.caution{font-size:7.6px;color:var(--muted);margin:14px 0 0 27px}
.footer{position:absolute;left:0;bottom:0;width:100%;height:86px}
.footer-band{position:absolute;left:0;top:0}
.footer-body{position:absolute;left:0;top:12px;width:100%;height:74px;background:var(--dark);padding:10px 14px 0 15px;color:#fff}
.site{display:flex;align-items:center;justify-content:center;gap:8px;font-size:8.6px;padding-bottom:8px;border-bottom:1px solid #888}
.site-icon{width:17px;height:17px;border-radius:50%;background:var(--red);display:flex;align-items:center;justify-content:center}
.foot-row{display:flex;justify-content:space-between;align-items:center;margin-top:6px;font-size:7.8px;white-space:nowrap}
.socials{display:flex;gap:4px}
.socials span{width:17px;height:17px;border:1.2px solid #fff;border-radius:50%}
</style>
</head>
<body>
<div class="browser-note">Is this email not displaying correctly?<br><a>View it in your browser.</a></div>

<section class="column col-one">
  <header class="brand">
    <span class="brand-mark"></span>
    <span class="brand-name">Harbour Lane Homes</span>
  </header>
  <div class="details">
    <div class="field-group">
      <h2 class="group-title">Today's Talent Oppurtunities</h2>
      <div class="field">Name:</div>
      <div class="field">Phone:</div>
      <div class="field">Mobile: *</div>
      <div class="field">Email: *</div>
      <div class="field">Mailing Address: *</div>
    </div>
    <div class="field-group">
      <h2 class="group-title">Land or property details:</h2>
      <div class="radio-line">Same as mailing address</div>
      <div class="field">Lot number (if applicable):</div>
      <div class="field">Unit number:</div>
      <div class="field">Street number:</div>
      <div class="field">Street name:</div>
      <div class="field">Suburb:</div>
      <div class="field">Estate name (if applicable) :</div>
    </div>
  </div>
  <div class="form">
    <p class="q">Client analysis questionnaire *</p>
    <p class="sub">How did you come across us?</p>
    <div class="opts">
      <div class="opt">o ( ) Search engine-website</div><div class="opt">o ( ) Site signage</div><div class="opt">o ( ) Ute signage</div><div class="opt">o ( ) Email marketing</div><div class="opt">o ( ) Flyer</div><div class="opt">o ( ) Business card</div><div class="opt">o ( ) Past client</div><div class="opt">o ( ) Referral</div><div class="opt">o ( ) Other:</div>
    </div>
    <div class="block">
      <p class="q">What does you enquiry relate to? *</p>
      <p class="sub">How did you come across us?</p>
      <div class="opt">o ( ) Passive house design, build &amp; certification</div><div class="opt">o ( ) New home design &amp; build with passive elements</div><div class="opt">o ( ) Extension with passive elements</div><div class="opt">o ( ) Renovation with passive elements</div><div class="opt">o ( ) Conventional new home design and build</div><div class="opt">o ( ) Conventional extension</div><div class="opt">o ( ) Conventional renovation</div><div class="opt">o ( ) Other:</div>
    </div>
    <div class="block">
      <p class="q">Have you obtained any plans or documentation for your project? *</p>
      <p class="small-q" style="font-weight:400">If you are unsure of your requirements please visit Home Building Advisory Office<br><span class="link">@ www.homebuildadvice.org</span></p>
      <div class="opt">o ( ) Yes</div><div class="opt">o ( ) No</div>
      <p class="small-q">If yes, please select from the following list to indicate what you have</p>
      <div class="opt">o ( ) Concept design(s)</div><div class="opt">o ( ) Planning permit</div><div class="opt">o ( ) Site feature and level survey</div>
      <div class="opt wrap">o ( ) Title boundary re-establishment survey( required if you wish to build to the boundary)</div>
      <div class="opt">o ( ) Engineering computations</div><div class="opt">o ( ) Geotechnical report</div><div class="opt">o ( ) Drainage plans</div><div class="opt">o ( ) Sewer details</div><div class="opt">o ( ) Stormwater/landfill information</div><div class="opt">o ( ) Energy rating report</div><div class="opt">o ( ) Electrical plan</div><div class="opt">o ( ) Internal joinery documentation</div><div class="opt">o ( ) Window schedule</div><div class="opt">o ( ) I have no idea what I have been given</div><div class="opt">o ( ) Other:</div>
    </div>
  </div>
</section>

<section class="column col-two">
  <div class="form">
    <p class="q">Have you engaged a Draftsman, Designer or Architect as yet?</p>
    <p class="hint">If yes, please provide their details below</p>
    <p class="q" style="margin-top:12px">When are you looking to commence your project? *</p>
    <div class="opt">o ( ) As soon as I find the right builder to work with</div><div class="opt">o ( ) 0-3 months time</div><div class="opt">o ( ) 6-12 months</div><div class="opt">o ( ) 1- 2 years time</div><div class="opt">o ( ) Are flexible and can work around Keystone Edge Homes</div><div class="opt">o ( ) Other:</div>
    <div class="block"><p class="q">For Extensions/Renovations-do you intend to move out during the works?</p>
    <div class="opt">o ( ) Yes</div><div class="opt">o ( ) No</div><div class="opt">o ( ) Not sure as yet</div></div>
    <div class="block" style="margin-top:10px"><p class="q">Do you have a budget in mind? *</p>
    <div class="opt">o ( ) Yes</div><div class="opt">o ( ) No</div><div class="opt">o ( ) Not sure as yet</div></div>
    <div class="block" style="margin-top:10px"><p class="q">Do you have your budget/finances organised? *</p>
    <div class="opt">o ( ) Yes</div><div class="opt">o ( ) No</div></div>
    <div class="block" style="margin-top:10px"><p class="q">Have you ever Built/Renovated or Extended before? *</p>
    <div class="opt">o ( ) Yes</div><div class="opt">o ( ) No</div></div>
    <div class="block" style="margin-top:18px"><p class="q">If yes, who was the Builder?<br>Are you speaking with them and are they quoting also?</p>
    <div class="opt">o ( ) Yes</div><div class="opt">o ( ) No</div></div>
    <div class="block" style="margin-top:18px"><p class="q">Have you spoken to any other Builder's in regards to your<br>proposed works? *</p>
    <div class="opt">o ( ) Yes</div><div class="opt">o ( ) No</div></div>
    <div class="block" style="margin-top:10px"><p class="q">Please provide a brief description of the works with anything<br>else you would like to add that may assist us with your enquiry</p>
    <p class="q" style="margin-top:5px">What do you need next in order to proceed with your proposed<br>project?</p>
    <p class="para">The planning and preparation stage is a time consuming process, however thorough detail is paramount. If we can gather as much information as we can now this will reduce any lengthly delays moving forward</p>
    <div class="opt">o ( ) An Architect/Designer/Draftsman to begin the process</div><div class="opt">o ( ) Discussion/advice relating to initial concept design</div><div class="opt">o ( ) Architectural documentation for the building permit</div><div class="opt">o ( ) Other additional documentation such as:</div><div class="opt">o ( ) Electrical plan</div><div class="opt">o ( ) Energy rating report</div><div class="opt">o ( ) Internal Joinery</div><div class="opt">o ( ) Window schedule</div><div class="opt">o ( ) Site level &amp; feature survey</div><div class="opt">o ( ) Title boundary re-establishment survey</div><div class="opt">o ( ) Geotechnical engineering</div><div class="opt">o ( ) Structural engineering</div><div class="opt">o ( ) Assistance with obtaining a building permit</div><div class="opt">o ( ) A cost analysis of our current plans and specifications*</div><div class="opt">o ( ) Other:</div>
    <p class="note">* Note: A fixed price cost analysis will only be obtained after the relevant parties enter into a preliminary agreement with the associated fee. In order for us to produce the most accurate price it is preferred that as many of the above documents be sourced where possible. If this is not feasible at this given point, a 'ballpark' estimate will be provided which will be non-binding in any form and be subject to final documentation being provided to Keystone Edge Homes. A thorough cost analysis will be provided back within one month or less after receiving payment and all the above documents. If not the preliminary agreement fee will be happily refunded no questions asked :) Regardless the preliminary</p>
    </div>
  </div>
</section>

<section class="column col-three">
  <p class="note">agreement fee will be happily refunded no questions asked :) Regardless the preliminary agreement fee will be deducted off the contract price should you wish to proceed with Keystone Edge Homes. Should you not, this fee is non-refundable. *</p>
  <p class="tick-title">Please tick to state you have read and agree with the above terms and conditions</p>
  <p class="agree">o ( ) I agree to the above terms and conditions and look forward to engaging Keystone Edge Homes</p>
  <div class="opt" style="height:auto;line-height:1.3">[ ] Send me a copy of my responses.</div>
  <a class="submit">Review and Submit</a>
  <p class="caution">Never submit passwords through online forms.</p>
  <footer class="footer">
    <svg class="footer-band" width="337" height="14" viewBox="0 0 337 14" aria-hidden="true"><polygon points="0,0 337,10 337,14 0,14" fill="#f3cdd2"/></svg>
    <div class="footer-body">
      <div class="site">
        <span class="site-icon"><svg width="9" height="7" viewBox="0 0 9 7" aria-hidden="true"><rect x=".5" y=".5" width="8" height="6" fill="#fff"/><path d="M.5 .8 4.5 4 8.5 .8" stroke="#e0232a" fill="none" stroke-width="1"/></svg></span>
        https://www.homebuildadvice.org/
      </div>
      <div class="foot-row">
        <span>Copyright © 2018 Harbour Lane Homes - All Rights Reserved.</span>
        <span class="socials"><span></span><span></span><span></span><span></span></span>
      </div>
    </div>
  </footer>
</section>
</body>
</html>
```